Educational Agency in Abu Dhabi looking for an 8 pages website

We are looking for an 8 pages design for a website, we already have one but we need to refine it and it is www.korvalendi.ae - Please base it on logo colours (attached) I have uploaded our logo, website content logo colors to use it for the scheme.
We are looking for a smooth look and content added if possible, I also attached content and logo

Industry/Entity Type

Education

Coding

Coded - Design and coding required

Number of Pages Required

5+ page

```html
<!DOCTYPE html>
<html lang="en">
<head>
<meta charset="utf-8">
<title>Korvalendi – Study Abroad</title>
<link href="https://fonts.googleapis.com/css2?family=Lato:wght@400;700;900&display=swap" rel="stylesheet">
<style>
:root{
  --orange:#f7901e;
  --navy:#1c2d6e;
  --ink:#222428;
  --body:#555a60;
  --muted:#8a8f96;
  --band:#f2f2f2;
  --footer:#1f2226;
  --footer-deep:#15171a;
  --white:#ffffff;
}
*{margin:0;padding:0;box-sizing:border-box}
html,body{width:1200px;height:3109px;overflow:hidden;background:var(--white)}
body{font-family:'Lato',sans-serif;color:var(--ink);position:relative}
.abs{position:absolute}

/* header */
.site-header{left:0;top:0;width:1200px;height:118px;background:var(--white)}
.brand{left:97px;top:38px;display:flex;align-items:center;gap:10px}
.brand-mark{width:22px;height:22px;background:var(--navy)}
.brand-name{font-weight:900;font-size:26px;color:var(--navy);letter-spacing:.5px}
.main-nav{right:86px;top:52px;display:flex;gap:30px;font-size:13.5px;font-weight:700;color:var(--navy)}
.main-nav .active{color:var(--orange)}

/* hero */
.hero{left:0;top:118px;width:1200px;height:566px;background:linear-gradient(180deg,#4b4a4c 0%,#6b625c 45%,#7d6a5a 75%,#5b544f 100%)}
.hero-shade{left:0;top:0;width:100%;height:100%;background:rgba(20,20,25,.35)}
.hero-title{left:0;top:104px;width:1200px;text-align:center;color:var(--white);font-weight:700;font-size:42px;line-height:59px}
.btn-primary{left:512px;top:323px;width:174px;height:52px;border-radius:26px;background:var(--orange);color:var(--white);font-weight:700;font-size:15px;display:flex;align-items:center;justify-content:center}

/* why card */
.why-card{left:85px;top:622px;width:1028px;height:404px;background:var(--white);box-shadow:0 4px 18px rgba(0,0,0,.12)}
.section-heading{font-weight:700;font-size:19px;color:var(--ink)}
.section-heading span{color:var(--orange)}
.why-heading{left:398px;top:42px;display:flex;align-items:center;gap:14px}
.why-heading i{display:block;width:86px;height:2px;background:var(--orange)}
.feature{width:300px;display:flex;gap:22px}
.feature svg{flex:none;width:38px;height:38px}
.feature h3{font-size:14.5px;font-weight:700;margin-bottom:8px;color:var(--ink)}
.feature p{font-size:10.5px;line-height:17px;color:var(--body)}

/* who */
.who-photo{left:87px;top:1098px;width:350px;height:353px;background:linear-gradient(135deg,#3d3a3a,#8d7c70 55%,#c9bfb6)}
.who-block{left:437px;top:1130px;width:83px;height:300px;background:var(--navy)}
.who-title{left:597px;top:1122px;font-size:29px;font-weight:700}
.who-title span{color:var(--orange)}
.who-text{left:597px;top:1182px;width:500px;font-size:11.5px;line-height:27px;color:var(--body)}
.who-text p+p{margin-top:20px}

/* destinations */
.destinations{left:0;top:1523px;width:1200px;height:564px;background:var(--band)}
.band-title{font-size:29px;font-weight:700}
.band-title span{color:var(--orange)}
.dest-card{top:143px;width:255px;height:303px;overflow:hidden}
.dest-tag{top:20px;left:-20px;position:absolute;background:var(--orange);color:var(--white);font-size:11.5px;font-weight:700;padding:10px 14px}
.dest-img{width:100%;height:100%}
.slide-arrow{left:84px;top:287px}
.dots{left:542px;top:489px;display:flex;gap:4px}
.dots i{display:block;width:36px;height:3px;background:#dcdcdc}
.dots i.on{background:var(--orange)}

/* news */
.news-title{left:85px;top:2150px}
.news-item{width:310px}
.news-date{display:flex;gap:24px}
.news-day{font-size:46px;font-weight:400;color:#c4c7cc;line-height:46px}
.news-mon{font-size:15px;color:#c4c7cc;margin-top:4px}
.news-head{font-size:20px;line-height:31px;color:var(--ink)}
.news-body{margin-top:48px;font-size:14.5px;line-height:25px;color:var(--muted)}
.btn-ghost{margin-top:48px;width:147px;height:42px;border:2px solid #d3d5d8;border-radius:21px;font-size:14px;color:var(--muted);display:flex;align-items:center;justify-content:center}

/* partners */
.partners-rule{left:99px;top:2632px;width:1002px;height:1px;background:#dcdde0}
.partner-arrow{top:2653px;width:29px;height:79px;background:var(--navy);display:flex;align-items:center;justify-content:center}
.partner-badge{top:2674px;width:96px;height:38px;border-radius:4px;background:#d5d7da}

/* footer */
.footer-rule{left:0;top:2823px;width:1200px;height:8px;background:var(--navy)}
.site-footer{left:0;top:2831px;width:1200px;height:220px;background:var(--footer);color:#c9ccd1}
.footer-col h4{font-size:15px;font-weight:700;color:var(--white);margin-bottom:22px}
.footer-col p{font-size:11.5px;line-height:17px;color:#9aa0a8}
.contact-row{display:flex;gap:14px;font-size:11.5px;line-height:17px;color:#9aa0a8;margin-bottom:12px}
.contact-row svg{flex:none;width:12px;height:12px;margin-top:2px}
.socials{display:flex;gap:6px;margin-top:16px}
.socials i{display:block;width:27px;height:27px;border-radius:50%}
.bottom-bar{left:0;top:3051px;width:1200px;height:58px;background:var(--footer-deep);color:#d5d8dc;font-size:11.5px}
</style>
</head>
<body>

<header class="abs site-header">
  <div class="abs brand"><span class="brand-mark"></span><span class="brand-name">KORVALENDI</span></div>
  <nav class="abs main-nav">
    <span class="active">Home</span><span>About us</span><span>Services</span><span>Why Study Abroad</span><span>Study Destinations</span><span>Study online</span><span>Apply Now</span><span>Contact Us</span>
  </nav>
</header>

<section class="abs hero" role="img" aria-label="Empty classroom with rows of wooden desks">
  <div class="abs hero-shade"></div>
  <h1 class="abs hero-title">Korvalendi is the number<br>one choice for students to<br>study abroad</h1>
  <div class="abs btn-primary">READ MORE</div>
</section>

<section class="abs why-card">
  <div class="abs why-heading"><h2 class="section-heading">Why Korvalendi <span>?</span></h2><i></i></div>

  <div class="abs feature" style="left:50px;top:108px">
    <svg viewBox="0 0 38 38" fill="none" stroke="#f7901e" stroke-width="2"><rect x="6" y="8" width="26" height="26"/><path d="M11 14h4M17 14h4M23 14h4M11 20h4M17 20h4M23 20h4M11 26h4M23 26h4M17 26v8"/></svg>
    <div><h3>Equipped Office</h3><p>We have well equipped office in Abu Dhabi managed by an experienced team with counseling and good knowledge in overseas education.</p></div>
  </div>
  <div class="abs feature" style="left:371px;top:108px">
    <svg viewBox="0 0 38 38" fill="none" stroke="#f7901e" stroke-width="2"><path d="M3 14l16-7 16 7-16 7z"/><path d="M10 18v9c5 4 13 4 18 0v-9M35 14v10"/></svg>
    <div><h3>Official tie up with Universities</h3><p>We officially represent Universities and institutions which provide top most infrastructure and quality education ensuring student satisfaction and positive results.</p></div>
  </div>
  <div class="abs feature" style="left:730px;top:108px">
    <svg viewBox="0 0 38 38" fill="none" stroke="#f7901e" stroke-width="2"><circle cx="19" cy="12" r="7"/><path d="M6 35c0-8 6-13 13-13s13 5 13 13"/></svg>
    <div><h3>Experienced Counselors</h3><p>We have counselors with extensive experience to guide students to fit into the right universities.</p></div>
  </div>
  <div class="abs feature" style="left:50px;top:261px">
    <svg viewBox="0 0 38 38" fill="none" stroke="#f7901e" stroke-width="2"><path d="M31 17a13 13 0 1 1-6-11"/><path d="M11 18l7 7 16-17"/></svg>
    <div><h3>Quality of Counseling</h3><p>We can assist with excellent, smart, smooth, and customized services for choosing the right course, getting admission, visa and arriving at the University.</p></div>
  </div>
  <div class="abs feature" style="left:371px;top:261px">
    <svg viewBox="0 0 38 38" fill="none" stroke="#f7901e" stroke-width="2"><path d="M8 4h16l7 7v23H8z"/><path d="M13 16h13M13 22h13M13 28h9"/></svg>
    <div><h3>Registration / License</h3><p>Korvalendi is registered with Ministry of Higher Education and various government and private sectors.</p></div>
  </div>
  <div class="abs feature" style="left:730px;top:261px">
    <svg viewBox="0 0 38 38" fill="none" stroke="#f7901e" stroke-width="2"><circle cx="19" cy="19" r="15"/><path d="M4 19h30M19 4c-6 7-6 23 0 30M19 4c6 7 6 23 0 30"/></svg>
    <div><h3>Range of Countries</h3><p>Our associated universities and institutions are in top world's top class cities of countries like UK, USA, CANADA, AUSTRALIA, MALAYSIA, GERMANY.</p></div>
  </div>
</section>

<div class="abs who-block"></div>
<div class="abs who-photo" role="img" aria-label="Students working together around a table"></div>
<h2 class="abs who-title">Who we <span>are?</span></h2>
<div class="abs who-text">
  <p>Korvalendi Abu Dhabi, one of the leading and fastest growing educational consulting company based in UAE officially recognized by Ministry of Higher Education and Scientific Research, Edvera Agency and ISO9001.</p>
  <p>Korvalendi was established in 2015 with an aim to provide professional consultancy services for the recruitment of quality international students to educational institutions based in UK, USA, Canada, Australia, Malaysia, Germany, Europe, Middle East and many more.</p>
</div>

<section class="abs destinations">
  <h2 class="abs band-title" style="left:85px;top:66px">Study <span>Destinations</span></h2>
  <svg class="abs slide-arrow" width="14" height="24" viewBox="0 0 14 24" fill="none" stroke="#777" stroke-width="2"><path d="M12 2L2 12l10 10"/></svg>

  <div class="abs dest-card" style="left:145px;overflow:visible">
    <div class="dest-img" role="img" aria-label="Student in front of a British flag" style="background:linear-gradient(135deg,#2b3f7a,#b53a46 50%,#e8dccd)"></div>
    <span class="dest-tag" style="left:-20px">Study in UK</span>
  </div>
  <div class="abs dest-card" style="left:423px;overflow:visible">
    <div class="dest-img" role="img" aria-label="Students holding an American flag" style="background:linear-gradient(180deg,#c9b48e,#8e7f6a 40%,#b5394a 70%,#2b3b73)"></div>
    <span class="dest-tag">Study in USA</span>
  </div>
  <div class="abs dest-card" style="left:700px;overflow:visible">
    <div class="dest-img" role="img" aria-label="Graduation cap on books over a map of Australia" style="background:linear-gradient(180deg,#ffffff 20%,#e9e6e3 45%,#2c3e7e 75%,#c9443f)"></div>
    <span class="dest-tag">Study in Australia</span>
  </div>
  <div class="abs dest-card" style="left:980px;width:220px;overflow:visible">
    <div class="dest-img" role="img" aria-label="Crossed New Zealand flags" style="background:linear-gradient(180deg,#ffffff,#eef0f4 30%,#34448a 55%,#ffffff 85%)"></div>
    <span class="dest-tag">Study in New Zealand</span>
  </div>

  <div class="abs dots"><i></i><i class="on"></i><i></i></div>
</section>

<h2 class="abs band-title news-title">News &amp; <span>Updates</span></h2>

<article class="abs news-item" style="left:87px;top:2252px">
  <div class="news-date"><div><div class="news-day">19</div><div class="news-mon">MAY</div></div><div class="news-head">Lorem ipsum dolor<br>dummy text</div></div>
  <p class="news-body">Lorem ipsum dolor sit amet, adipiscing elit, sed do eiusmod tempor incididunt ut labore et dolore magna aliqua. Ut enim .</p>
  <div class="btn-ghost">Read More</div>
</article>
<article class="abs news-item" style="left:439px;top:2252px">
  <div class="news-date"><div><div class="news-day">20</div><div class="news-mon">MAY</div></div><div class="news-head">Lorem ipsum dolor<br>dummy text</div></div>
  <p class="news-body">Lorem ipsum dolor sit amet, adipiscing elit, sed do eiusmod tempor incididunt ut labore et dolore magna aliqua. Ut enim .</p>
  <div class="btn-ghost">Read More</div>
</article>
<article class="abs news-item" style="left:790px;top:2252px">
  <div class="news-date"><div><div class="news-day">21</div><div class="news-mon">MAY</div></div><div class="news-head">Lorem ipsum dolor<br>dummy text</div></div>
  <p class="news-body">Lorem ipsum dolor sit amet, adipiscing elit, sed do eiusmod tempor incididunt ut labore et dolore magna aliqua. Ut enim .</p>
  <div class="btn-ghost">Read More</div>
</article>

<div class="abs partners-rule"></div>
<div class="abs partner-arrow" style="left:99px"><svg width="8" height="12" viewBox="0 0 8 12" fill="none" stroke="#fff" stroke-width="1.6"><path d="M6 1L1 6l5 5"/></svg></div>
<div class="abs partner-badge" style="left:168px"></div>
<div class="abs partner-badge" style="left:318px"></div>
<div class="abs partner-badge" style="left:470px"></div>
<div class="abs partner-badge" style="left:628px"></div>
<div class="abs partner-badge" style="left:778px"></div>
<div class="abs partner-badge" style="left:930px"></div>
<div class="abs partner-arrow" style="left:1071px"><svg width="8" height="12" viewBox="0 0 8 12" fill="none" stroke="#fff" stroke-width="1.6"><path d="M2 1l5 5-5 5"/></svg></div>

<div class="abs footer-rule"></div>
<footer class="abs site-footer">
  <div class="abs footer-col" style="left:99px;top:36px;width:250px">
    <h4>ABOUT</h4>
    <p>Our counseling services focus on student careers making sure that they are well placed in good and reputed institutions overseas.</p>
  </div>
  <div class="abs footer-col" style="left:423px;top:36px;width:300px">
    <h4>GET IN TOUCH</h4>
    <div class="contact-row"><svg viewBox="0 0 12 12" fill="#f7901e"><path d="M6 0a4 4 0 0 0-4 4c0 3 4 8 4 8s4-5 4-8a4 4 0 0 0-4-4zm0 5.5A1.5 1.5 0 1 1 6 2.5a1.5 1.5 0 0 1 0 3z"/></svg><span>Harbor Gate Tower, Suite 31, 3rd Floor,<br>PO Box – 4720</span></div>
    <div class="contact-row"><svg viewBox="0 0 12 12" fill="#f7901e"><path d="M2.5 0.5l2 2.5-1.2 1.5a7 7 0 0 0 4.2 4.2L9 7.5l2.5 2-1.5 2C5 11 1 7 0.5 2z"/></svg><span>+971 2 555 01 42</span></div>
    <div class="contact-row"><svg viewBox="0 0 12 12" fill="#f7901e"><path d="M0 2h12v8H0z"/><path d="M0 2l6 4 6-4" stroke="#1f2226" fill="none"/></svg><span>info@korvalendi.ae</span></div>
  </div>
  <div class="abs footer-col" style="left:803px;top:36px;width:300px">
    <h4>GET IN TOUCH</h4>
    <p>Labore quis ut venison ball tip short ribs eiusmod minim nulla, irure ipsum pork belly fatback volup</p>
    <div class="socials"><i style="background:#3b5998"></i><i style="background:#d32f2f"></i><i style="background:#dd4b39"></i><i style="background:#0e76a8"></i></div>
  </div>
</footer>
<div class="abs bottom-bar">
  <span class="abs" style="left:85px;top:21px">© Copyright 2018.  All rights reserved.</span>
  <span class="abs" style="left:915px;top:21px">Terms &amp; conditions</span>
  <span class="abs" style="left:1040px;top:21px">Privacy policy</span>
</div>

</body>
</html>
```